Creative & Professional Business Card for hair salon

We are looking to update our business cards. Our salon is creative, modern, progressive and professional and looking for a design that will reflect this.

```html
<!DOCTYPE html>
<html lang="en">
<head>
<meta charset="utf-8">
<title>Minds in the Mist – Business Card</title>
<link rel="stylesheet" href="https://fonts.googleapis.com/css2?family=Quicksand:wght@300&family=Montserrat:wght@600&display=swap">
<style>
  :root {
    --stage: #000000;
    --paper: #ffffff;
    --ink: #4a6b80;
    --ink-strong: #3e5b6e;
    --icon-bg: #4cb0d8;
    --rule: #1a6fc0;
    --wash-deep: #2f7fc0;
    --wash-mid: #5fb0dc;
    --wash-light: #a9d8ef;
    --teal: #3aa6b8;
  }
  * { box-sizing: border-box; margin: 0; padding: 0; }
  html, body {
    width: 1200px; height: 1200px; overflow: hidden;
    background: var(--stage);
  }
  .canvas { position: relative; width: 1200px; height: 1200px; }

  .card {
    position: absolute; background: var(--paper); overflow: hidden;
  }
  .card--front { left: 178px; top: 84px; width: 840px; height: 480px; }
  .card--back  { left: 178px; top: 634px; width: 838px; height: 480px; }

  .wash { position: absolute; left: 0; top: 0; width: 840px; height: 480px; }

  .name-frame {
    position: absolute; left: 169px; top: 103px; width: 503px; height: 271px;
    border: 3px solid var(--paper);
    padding: 5px 13px;
  }
  .name-panel {
    width: 100%; height: 100%; background: var(--paper);
    display: flex; flex-direction: column; align-items: flex-end; justify-content: center;
    padding: 0 16px 0 0;
    font-family: "Quicksand", sans-serif; font-weight: 300; color: var(--ink);
  }
  .name-panel .brand { font-size: 46px; line-height: 1.1; letter-spacing: -0.5px; }
  .name-panel .owner { font-size: 24px; line-height: 1.4; }

  .orb { position: absolute; left: -247px; top: 0; width: 480px; height: 480px; }

  .contact-rule {
    position: absolute; left: 268px; top: 62px; width: 3px; height: 330px;
    background: var(--rule);
  }
  .contact { position: absolute; left: 279px; display: flex; align-items: flex-start; }
  .contact__icon {
    width: 42px; height: 42px; background: var(--icon-bg); flex: none;
    display: flex; align-items: center; justify-content: center;
  }
  .contact__text {
    margin-left: 33px;
    font-family: "Montserrat", sans-serif; font-weight: 600;
    font-size: 22px; line-height: 32px; color: var(--ink-strong);
    letter-spacing: 0.6px;
  }
  .contact__text p + p { margin-top: 14px; }
  .contact--place { top: 66px; }
  .contact--phone { top: 173px; }
  .contact--web   { top: 261px; }
</style>
</head>
<body>
<main class="canvas">

  <section class="card card--front">
    <svg class="wash" viewBox="0 0 840 480" role="img" aria-label="Blue watercolour splash behind the salon name">
      <defs>
        <radialGradient id="washFill" cx="0.35" cy="0.35" r="0.75">
          <stop offset="0" stop-color="var(--wash-deep)"/>
          <stop offset="0.45" stop-color="var(--wash-mid)"/>
          <stop offset="1" stop-color="var(--wash-light)"/>
        </radialGradient>
      </defs>
      <path fill="url(#washFill)" d="M40 170 C60 120 120 90 190 100 C240 70 330 60 420 30 C480 0 580 10 650 30 C700 40 720 100 700 140 C760 150 810 200 810 250 C790 300 740 330 740 390 C720 450 650 470 560 480 L240 480 C200 460 190 420 150 400 C100 380 80 330 60 290 C40 250 30 210 40 170 Z"/>
    </svg>
    <div class="name-frame">
      <div class="name-panel">
        <div class="brand">Minds in the Mist</div>
        <div class="owner">by Tara Vell</div>
      </div>
    </div>
  </section>

  <section class="card card--back">
    <svg class="orb" viewBox="0 0 480 480" role="img" aria-label="Blue and teal watercolour circle">
      <defs>
        <linearGradient id="orbFill" x1="0" y1="0" x2="0.4" y2="1">
          <stop offset="0" stop-color="var(--wash-mid)"/>
          <stop offset="0.45" stop-color="var(--wash-deep)"/>
          <stop offset="1" stop-color="var(--teal)"/>
        </linearGradient>
      </defs>
      <circle cx="240" cy="240" r="240" fill="url(#orbFill)"/>
    </svg>

    <div class="contact-rule"></div>

    <div class="contact contact--place">
      <div class="contact__icon">
        <svg width="24" height="30" viewBox="0 0 24 30" aria-hidden="true">
          <path d="M12 2 C6 2 2.5 6.5 2.5 11.5 C2.5 18 12 28 12 28 C12 28 21.5 18 21.5 11.5 C21.5 6.5 18 2 12 2 Z" fill="none" stroke="#fff" stroke-width="2.5"/>
          <circle cx="12" cy="11" r="4" fill="#fff"/>
        </svg>
      </div>
      <div class="contact__text">5/12 Harlow Street,<br>Penbrook.</div>
    </div>

    <div class="contact contact--phone">
      <div class="contact__icon">
        <svg width="28" height="28" viewBox="0 0 28 28" aria-hidden="true">
          <path d="M6 3 L10 3 L12 9 L9 11 C10.5 15 13 17.5 17 19 L19 16 L25 18 L25 22 C25 24 23 25 21 25 C12 24 4 16 3 7 C3 5 4 3 6 3 Z" fill="#fff"/>
        </svg>
      </div>
      <div class="contact__text">07 5012 3348</div>
    </div>

    <div class="contact contact--web">
      <div class="contact__icon">
        <svg width="30" height="30" viewBox="0 0 30 30" aria-hidden="true" fill="none" stroke="#fff" stroke-width="2">
          <circle cx="15" cy="15" r="12"/>
          <ellipse cx="15" cy="15" rx="5.5" ry="12"/>
          <line x1="3" y1="15" x2="27" y2="15"/>
          <line x1="5" y1="9" x2="25" y2="9"/>
          <line x1="5" y1="21" x2="25" y2="21"/>
          <line x1="15" y1="3" x2="15" y2="27"/>
        </svg>
      </div>
      <div class="contact__text">
        <p>E-salon@mindsinthemist.com.au</p>
        <p>W-www.mindsinthemist.com.au</p>
        <p>F-www.social.com/MindsInThe-<br>Mist byTaraVell</p>
      </div>
    </div>
  </section>

</main>
</body>
</html>
```